Copper Heron Bar & Grill Takeout Menu

Please create a takeout menu using the attached dine-in menu.
Take out menu size: Tri-Fold 11x17

Industry/Entity Type

Bar & Grill (Restaurant)

Colors

Designer to choose colors to be used in the design.

Requirements
Must have
• Phone number and website. "Order Online" "Order for Delivery"
Nice to have
• Area on the back of the menu to feature happy hour specials.

```html
<!DOCTYPE html>
<html lang="en">
<head>
<meta charset="utf-8">
<title>Copper Heron Bar &amp; Grill — Takeout Menu</title>
<link href="https://fonts.googleapis.com/css2?family=IM+Fell+English+SC&family=Montserrat:wght@400;600;700&family=Great+Vibes&family=Bangers&display=swap" rel="stylesheet">
<style>
:root{
  --paper:#ecebe4;
  --paper-edge:#d9d8cf;
  --ink:#1d1d1d;
  --brown:#6b2a12;
  --cyan:#4fd0e3;
  --cyan-dark:#1ea9bf;
  --purple:#2a1160;
  --purple-deep:#180836;
  --violet:#5b2ca8;
  --pink:#ff2fa6;
  --yellow:#ffe600;
  --leaf:#5cb531;
  --chili:#e2331f;
  --page:#ffffff;
}
*{box-sizing:border-box;margin:0;padding:0}
html,body{width:1200px;height:2370px;overflow:hidden;background:var(--page)}
body{font-family:'Montserrat',sans-serif;color:var(--ink);position:relative}
.spread{position:absolute;left:40px;width:1120px;height:730px;display:flex;box-shadow:0 14px 28px rgba(0,0,0,.18)}
.spread--outside{top:400px}
.spread--inside{top:1220px}
.panel{width:373.33px;height:100%;background:radial-gradient(circle at 50% 40%,var(--paper) 60%,var(--paper-edge));padding:42px 30px 30px;position:relative}
.panel--purple{background:linear-gradient(180deg,var(--purple-deep),var(--purple) 45%,var(--violet) 70%,var(--purple-deep));padding:44px 34px}
.heading{font-family:'IM Fell English SC',serif;font-size:40px;line-height:1;color:var(--ink);display:flex;align-items:center;gap:10px;border-bottom:2px solid var(--ink);padding-bottom:6px;margin-bottom:12px}
.heading--sm{font-size:28px;border:0;margin:8px 0 4px;padding:0}
.food-art{display:inline-block;border-radius:50%}
.item{display:flex;align-items:baseline;font-size:11.5px;font-weight:700;margin-top:7px}
.item .leader{flex:1;border-bottom:1.5px dotted #444;margin:0 4px}
.price{background:var(--cyan);color:#fff;font-size:9.5px;font-weight:700;min-width:34px;text-align:center;border-radius:2px;padding:1px 0;margin-left:8px}
.desc{font-size:7.6px;line-height:1.3;color:#333;margin-top:2px;margin-right:50px}
.veg{display:inline-block;width:7px;height:7px;background:var(--leaf);border-radius:0 6px 0 6px;margin-left:3px}
.spicy{display:inline-block;width:4px;height:9px;background:var(--chili);border-radius:3px;margin-left:2px;transform:rotate(25deg)}
.add-box{border:1.5px solid var(--ink);padding:6px 14px 10px;margin-top:16px;position:relative}
.add-title{font-family:'Great Vibes',cursive;font-size:22px;line-height:1}
.add-box .item{margin-right:50px;margin-top:4px}
.skewer{position:absolute;right:12px;top:12px;width:20px;height:62px;background:linear-gradient(#e3532a,#c23719);border-radius:10px}
.band{height:7px;border-top:1px solid #555;border-bottom:1px solid #555;background:repeating-linear-gradient(90deg,#777 0 2px,transparent 2px 5px);margin:12px 0 4px}
.script{font-family:'Great Vibes',cursive;font-size:28px;line-height:1.1}
.small-bold{font-size:8px;font-weight:700;line-height:1.35}
.notice{background:#050505;color:#fff;text-align:center;padding:8px 10px;margin-top:12px;border-radius:2px}
.notice p{font-family:'IM Fell English SC',serif;font-size:8px;line-height:1.25}
.notice .key{font-size:7px;margin-top:4px;font-family:'Montserrat',sans-serif}
.frame{border:3px double #b8b3cc;outline:1px solid #8e86b4;outline-offset:3px;height:100%;padding:14px 16px;display:flex;flex-direction:column}
.frame--light{border-color:#444;outline-color:#777;background:transparent}
.frame-title{font-family:'IM Fell English SC',serif;font-size:22px;text-align:center;color:#fff;line-height:1.05;margin-bottom:10px}
.panel--purple .item{color:#fff;font-size:11px}
.panel--purple .desc{color:#e7e0ff;margin-right:0}
.cup{color:var(--cyan);font-size:9px;font-weight:700}
.add-line{border:1px solid #d9d3f3;color:#fff;font-size:8.5px;font-weight:700;padding:4px 8px;margin-top:12px;display:flex;align-items:center;gap:6px}
.add-line .add-title{font-size:18px}
.happy{position:relative;height:120px;margin-top:20px}
.happy-text{font-family:'Bangers',cursive;font-size:38px;line-height:.9;transform:rotate(-8deg);position:absolute;left:8px;top:16px}
.happy-text .pink{color:var(--pink)}
.happy-text .yel{color:var(--yellow)}
.clock{position:absolute;right:14px;top:4px}
.beer-art{height:130px;width:150px;margin:4px auto 0;border-radius:12px;background:radial-gradient(circle at 50% 60%,#f4b623,#b87612 55%,transparent 75%)}
.contact-btn{background:var(--cyan);color:var(--purple-deep);font-family:'IM Fell English SC',serif;font-size:20px;text-align:center;border-radius:18px;width:190px;margin:16px auto 8px;padding:2px 0}
.contact-line{display:flex;align-items:center;gap:8px;color:#fff;font-weight:600;font-size:15px;margin:5px 0 0 4px}
.cover{text-align:center;padding-top:38px}
.brand-mark{font-family:'IM Fell English SC',serif;font-size:30px;line-height:1.05;color:var(--ink);display:flex;align-items:center;justify-content:center;gap:10px}
.brand-mark .dot{width:16px;height:16px;border-radius:50%;background:var(--ink)}
.cover-art{width:240px;height:240px;border-radius:50%;margin:20px auto 16px;background:radial-gradient(circle at 50% 45%,#7a63c4 0 30%,#c8a030 45%,#7b3a18 70%,#4a1f0c)}
.cover-name{font-family:'IM Fell English SC',serif;font-size:38px;line-height:1.02}
.cover-name .line2{color:var(--brown)}
.order-btn{display:inline-block;background:var(--cyan);color:var(--brown);font-family:'IM Fell English SC',serif;font-size:17px;padding:4px 22px;border-radius:16px;margin-top:18px;box-shadow:0 0 0 3px rgba(79,208,227,.35)}
.cover-url{font-size:11px;margin-top:12px}
.tab{display:inline-block;background:#151515;color:#fff;font-family:'IM Fell English SC',serif;font-size:11px;padding:1px 10px;margin-top:10px;clip-path:polygon(4% 0,100% 0,96% 100%,0 100%)}
.starters .item{margin-top:4px;font-size:10.5px}
.starters .heading{margin-bottom:4px}
.burgers .frame-title{color:var(--ink)}
.intro{font-size:7.4px;line-height:1.3;text-align:center;color:#333}
.bun{display:flex;justify-content:space-between;align-items:center;background:#0a0a0a;color:#fff;font-size:7.5px;font-weight:700;padding:3px 6px;margin-top:6px}
.bun .icons{display:flex;gap:14px}
.bun .icons span{width:10px;height:10px;border-radius:50%}
.bgrow{display:flex;align-items:flex-start;margin-top:5px}
.bgrow .bname{flex:1;font-size:9px;font-weight:700}
.bgrow .bname .desc{font-weight:400;font-size:7px;margin:1px 0 0}
.bgrow .price{min-width:22px;font-size:8px;margin-left:10px}
.handhelds .heading{font-size:30px}
.boxes{display:grid;grid-template-columns:1fr 1fr;gap:6px;margin-top:14px}
.box{border:1.5px solid var(--ink);padding:4px 6px}
.box h4{font-family:'IM Fell English SC',serif;font-weight:400;font-size:14px}
.box p{font-size:7px;line-height:1.3}
.box--wide{grid-column:span 2}
</style>
</head>
<body>

<section class="spread spread--outside">
  <div class="panel salads">
    <h2 class="heading">SALADS <span class="food-art" role="img" aria-label="Salad bowl illustration" style="width:70px;height:24px;background:linear-gradient(#4f9f2c,#c8e0b0)"></span></h2>
    <div class="item"><span>Combo Cat</span><span class="leader"></span><span class="price">11</span></div>
    <p class="desc">Enjoy a side House and a cup of any soup</p>
    <div class="item"><span>Cat House Salad<i class="veg"></i></span><span class="leader"></span><span class="price">11</span></div>
    <p class="desc">Spring lettuce mix, fresh red peppers, onion, cherry tomatoes, cucumber, and croutons. Served with Red Wine Vinaigrette</p>
    <div class="item"><span>Grilled Chicken Salad</span><span class="leader"></span><span class="price">15</span></div>
    <p class="desc">Spring lettuce mix, grilled chicken breast, bacon, fresh red peppers, onions, tomatoes, cucumber and feta cheese. Served with Red Wine Vinaigrette</p>
    <div class="item"><span>Grilled Shrimp Salad*</span><span class="leader"></span><span class="price">16</span></div>
    <p class="desc">Spring lettuce mix, garlic Roasted Shrimp, roasted corn, pico de gallo fresh avocado, Served with Lemon Champagne Vinaigrette</p>
    <div class="item"><span>Goat Cheese Salad<i class="veg"></i></span><span class="leader"></span><span class="price">16</span></div>
    <p class="desc">Spring lettuce mix, fried goat cheese, fresh red peppers, cranberries, white onions, and cherry tomatoes. Served with Lemon Champagne Vinaigrette</p>
    <div class="item"><span>The Skinny Cat<i class="veg"></i></span><span class="leader"></span><span class="price">14</span></div>
    <p class="desc">Spring lettuce mix, sliced apple, sun dried cranberries, roasted corn, cherry tomatoes and feta cheese. Served with Balsamic Vinaigrette</p>
    <div class="item"><span>Small House Salad<i class="veg"></i></span><span class="leader"></span><span class="price">6</span></div>
    <div class="add-box">
      <div class="add-title">Add</div>
      <div class="item"><span>Grilled Chicken</span><span class="leader"></span><span class="price">5</span></div>
      <div class="item"><span>Garlic Roasted Shrimp</span><span class="leader"></span><span class="price">5</span></div>
      <div class="item"><span>Fried Goat Cheese</span><span class="leader"></span><span class="price">4</span></div>
      <span class="skewer" role="img" aria-label="Shrimp skewer illustration"></span>
    </div>
    <div class="band"></div>
    <div class="script">Dressings <span class="food-art" role="img" aria-label="Herb sprig illustration" style="width:50px;height:16px;background:#6aa83a"></span></div>
    <p class="small-bold">Balsamic Vinaigrette | Caesar | Red Wine Vinaigrette | Honey-Mustard Lemon Champagne Vinaigrette | Ranch | Blue Cheese</p>
    <div class="notice">
      <p>The consumption of raw or undercooked eggs, meat, poultry, seafood or shellfish may contribute to food borne illness, especially if you have a medical condition.</p>
      <p class="key"><i class="veg"></i> Vegetarian &nbsp; <i class="spicy"></i> Spicy</p>
    </div>
  </div>

  <div class="panel panel--purple">
    <div class="frame">
      <h3 class="frame-title">SOUPS &amp; BOWLS</h3>
      <div class="item"><span>Copper Heron Chili</span><span class="leader" style="border:0"></span><span class="cup">CUP 6 | BOWL 8</span></div>
      <p class="desc">Copper Heron Signature Chili with lean ground beef, black beans, and corn. Topped with cheddar cheese and green onion, served with tri-color tortilla chips</p>
      <div class="item"><span>Ancient Grains Bowl</span><span class="leader" style="border-color:#ddd"></span><span class="cup">12</span></div>
      <p class="desc">Quinoa, brown rice, kale and fresh spinach, with fire roasted portobello mushrooms, zucchini and red peppers. Topped with fresh avocado, and feta cheese. Served with Lemon Champagne Vinaigrette</p>
      <div class="add-line"><span class="add-title">Add:</span> Grilled Chicken 5 | Garlic Roasted Shrimp 5</div>
      <div class="happy">
        <div class="happy-text"><span class="pink">HAPPY<br>HOUR</span><br><span class="yel">SPECIALS</span></div>
        <svg class="clock" width="80" height="80" viewBox="0 0 80 80" fill="none" stroke="#4fd0e3" stroke-width="3"><path d="M14 40a26 26 0 1 0 8-19"/><path d="M22 8v13h13"/><path d="M40 24v17h12"/></svg>
      </div>
      <div class="beer-art" role="img" aria-label="Two beer mugs with confetti illustration"></div>
      <div class="contact-btn">CONTACT US</div>
      <div class="contact-line"><svg width="16" height="16" viewBox="0 0 24 24" fill="#fff"><path d="M6.6 10.8a15 15 0 0 0 6.6 6.6l2.2-2.2a1 1 0 0 1 1-.25 11.4 11.4 0 0 0 3.6.57 1 1 0 0 1 1 1V20a1 1 0 0 1-1 1A17 17 0 0 1 3 4a1 1 0 0 1 1-1h3.5a1 1 0 0 1 1 1c0 1.25.2 2.45.57 3.57a1 1 0 0 1-.25 1z"/></svg>555-014-2286</div>
      <div class="contact-line"><svg width="16" height="16" viewBox="0 0 24 24" fill="none" stroke="#fff" stroke-width="2"><circle cx="12" cy="12" r="10"/><path d="M2 12h20M12 2a15 15 0 0 1 0 20M12 2a15 15 0 0 0 0 20"/></svg>www.copperherongrill.com</div>
    </div>
  </div>

  <div class="panel cover">
    <div class="brand-mark"><span class="dot"></span><span>Copper Heron<br>Bar &amp; Grill</span></div>
    <div class="cover-art" role="img" aria-label="Round illustration of two bar characters sharing drinks"></div>
    <h1 class="cover-name">COPPER HERON<br><span class="line2">BAR &amp; GRILL</span></h1>
    <div class="order-btn">ORDER FOR DELIVERY</div>
    <p class="cover-url">www.<b>copperherongrill</b>.com</p>
  </div>
</section>

<section class="spread spread--inside">
  <div class="panel starters">
    <h2 class="heading">STARTERS <span class="food-art" role="img" aria-label="Chips and dip illustration" style="width:54px;height:22px;background:linear-gradient(#f0a22a,#d9661e)"></span></h2>
    <span class="tab">TORTILLA CHIPS</span>
    <div class="item"><span>with House-made Salsa Verde<i class="veg"></i><i class="spicy"></i></span><span class="leader"></span><span class="price">11</span></div>
    <div class="item"><span>with House-made Fire Roasted Salsa<i class="veg"></i></span><span class="leader"></span><span class="price">11</span></div>
    <div class="item"><span>with Guacamole &amp; Pico De Gallo<i class="veg"></i></span><span class="leader"></span><span class="price">15</span></div>
    <div class="item"><span>with Queso<i class="veg"></i></span><span class="leader"></span><span class="price">16</span></div>
    <div class="item"><span>with Chili con Queso</span><span class="leader"></span><span class="price">16</span></div>
    <span class="tab">WINGS</span>
    <div class="item"><span>8 pieces</span><span class="leader"></span><span class="price">14</span></div>
    <p class="desc">Flash-fried to a crispy golden brown and tossed in your choice of sauce. Choose from our Signature Hot, or Mild Sauce, or BBQ. Your choice of ranch or blue cheese.</p>
    <span class="tab">QUESADILLAS</span>
    <div class="item"><span>Cheddar and Monterey Jack Cheese<i class="veg"></i></span><span class="leader"></span><span class="price">11</span></div>
    <div class="item"><span>Pulled Marinated Chicken &amp; Cheese</span><span class="leader"></span><span class="price">11</span></div>
    <div class="item"><span>Fire Roasted Vegetables &amp; Cheese<i class="veg"></i></span><span class="leader"></span><span class="price">15</span></div>
    <div class="item"><span>Garlic Roasted Shrimp &amp; Cheese</span><span class="leader"></span><span class="price">16</span></div>
    <p class="desc">All quesadillas are stuffed with roasted red peppers, black beans and your choice below. Served with guacamole, pico de gallo, and chipotle crema on the side</p>
    <span class="tab">CLAW-FULL NACHOS</span>
    <p class="desc">Tortilla chips, melted white queso, Cheddar and Monterey Jack cheeses, pico de gallo, guacamole, chipotle sour cream, jalapenos, black beans, &amp; green onions</p>
    <div class="item"><span>Copper Heron Chili Nachos</span><span class="leader"></span><span class="price">11</span></div>
    <div class="item"><span>Pulled Chicken Nachos</span><span class="leader"></span><span class="price">11</span></div>
    <div class="item"><span>Garlic Roasted Shrimp</span><span class="leader"></span><span class="price">15</span></div>
    <div class="item"><span>Fire Roasted Vegetables Nachos<i class="veg"></i></span><span class="leader"></span><span class="price">16</span></div>
    <span class="tab">FRENCH FRIES</span>
    <p class="desc">Served with our house made Garlic Aioli and Spicy Ketchup.</p>
    <div class="item"><span>Fries Only<i class="veg"></i></span><span class="leader"></span><span class="price">11</span></div>
    <div class="item"><span>Sweet Potato Fries<i class="veg"></i></span><span class="leader"></span><span class="price">11</span></div>
    <div class="item"><span>Cheddar-Jack Cheese Fries<i class="veg"></i></span><span class="leader"></span><span class="price">11</span></div>
    <div class="item"><span>Cheddar-Jack Cheese, Bacon Fries</span><span class="leader"></span><span class="price">11</span></div>
  </div>

  <div class="panel burgers" style="padding:44px 34px">
    <div class="frame frame--light">
      <h3 class="frame-title">GOURMET BURGERS &amp;<br>SANDWICHES</h3>
      <p class="intro">Start with your style and then choose your protein. Our burgers are house made and cooked to your temperature. Our fresh grilled chicken breast is marinated in house and cooked to perfection. Keep it vegetarian by choosing a vegetarian style along with the Quinoa Lentil Burger. All are served on a potato bun with lettuce, tomato, onion, and your choice of hand cut fries or sweet potato fries.</p>
      <p class="intro" style="font-weight:700;font-size:8px;margin-top:6px">Premium sides available for an up charge + $2</p>
      <div class="bun"><span>Gluten-Free Bun Available<br>Upon Request | $2</span><span class="icons"><span style="background:#e0542a"></span><span style="background:#f2c230"></span><span style="background:var(--leaf)"></span></span></div>
      <div class="bgrow"><div class="bname">Calico Cat<i class="veg"></i><p class="desc">Roasted red peppers, red onions, brie cheese, and horseradish aioli</p></div><span class="price">14</span><span class="price">14</span><span class="price">14</span></div>
      <div class="bgrow"><div class="bname">Tiger Cat<i class="veg"></i><p class="desc">Cheddar, Monterey Jack, and Provolone</p></div><span class="price">14</span><span class="price">14</span><span class="price">14</span></div>
      <div class="bgrow"><div class="bname">Cat Scratch Fever<i class="veg"></i><p class="desc">Guacamole, 3 pepper colby jack, pico de gallo, and chipotle mayo</p></div><span class="price">14</span><span class="price">14</span><span class="price">14</span></div>
      <div class="bgrow"><div class="bname">The Fat Cat<p class="desc">Fried egg*, bacon, cheddar cheese, and garlic aioli</p></div><span class="price">14</span><span class="price">14</span><span class="price">14</span></div>
      <div class="bgrow"><div class="bname">Tabby Cat<i class="veg"></i><p class="desc">Melted brie cheese, sliced apple, and citrus aioli</p></div><span class="price">14</span><span class="price">14</span><span class="price">14</span></div>
      <div class="bgrow"><div class="bname">The Sphynx<i class="veg"></i><p class="desc">Portobello mushrooms, roasted red peppers, smoked gouda cheese, and roasted garlic aioli</p></div><span class="price">14</span><span class="price">14</span><span class="price">14</span></div>
      <div class="bgrow"><div class="bname">Maine Coon<p class="desc">Grilled shrimp*, roasted corn, swiss cheese, and roasted garlic aioli</p></div><span class="price">14</span><span class="price">14</span><span class="price">14</span></div>
      <div class="bgrow"><div class="bname">Alley Cat<i class="veg"></i><p class="desc">Whats up your alley? Choose a cheese, condiment and one topping.<br><b>Additional Toppings $1<br>Bacon, Egg, Shrimp - $2</b></p></div><span class="price">14</span><span class="price">14</span><span class="price">14</span></div>
      <div class="notice">
        <p>The consumption of raw or undercooked eggs, meat, poultry, seafood or shellfish may contribute to food borne illness, especially if you have a medical condition.</p>
        <p class="key"><i class="veg"></i> Vegetarian &nbsp; <i class="spicy"></i> Spicy</p>
      </div>
    </div>
  </div>

  <div class="panel handhelds">
    <h2 class="heading" style="border:0;margin-bottom:2px">OTHER HANDHELDS</h2>
    <p class="desc" style="margin:0">All served with Hand Cut Fries or Sweet Potato Fries.</p>
    <p class="small-bold">Premium sides available for an up charge +2</p>
    <div class="item"><span>Cat Club</span><span class="leader"></span><span class="price">11</span></div>
    <p class="desc">Sliced whole wheat bread with roasted garlic aioli, grilled marinated chicken breast, provolone cheese bacon, lettuce and tomato</p>
    <div class="item"><span>Southwest Melt</span><span class="leader"></span><span class="price">11</span></div>
    <p class="desc">Sliced whole wheat bread with roasted garlic aioli, 3 pepper colby jack, roasted red peppers and corn</p>
    <div class="item"><span>What's Gouda?</span><span class="leader"></span><span class="price">11</span></div>
    <p class="desc">Sliced whole wheat bread with roasted garlic aioli smoked gouda and provolone cheeses, roasted red peppers and portobello mushrooms</p>
    <div class="item"><span>Westover Melt</span><span class="leader"></span><span class="price">11</span></div>
    <p class="desc">Sliced whole wheat bread with roasted garlic aioli, zucchini, portobello mushrooms, red peppers, with melted brie and provolone cheeses</p>
    <div class="boxes">
      <div class="box"><h4>CHEESES</h4><p>Vermont Cheddar | Smoked Gouda | 3-Pepper Colby Jack Monterey Jack | Swiss | Brie Provolone | American</p></div>
      <div class="box"><h4>CONDIMENTS</h4><p>Horseradish Aioli | Chipotle Crema Roasted Garlic Aioli | Citrus Aioli Spicy Ketchup | Dijon Mustard | Yellow Mustard | Mayo | Ketchup</p></div>
      <div class="box box--wide"><h4>TOPPINGS</h4><p>Bacon | Shrimp | Egg | Red Onion | White Onion | Portobello Mushrooms Roasted Corn | Roasted Red Peppers Guacamole | Pico De Gallo | Fresh or Pickled Jalapenos</p></div>
    </div>
    <div class="band"></div>
    <h3 class="heading heading--sm">SIDES <span class="food-art" role="img" aria-label="Fries illustration" style="width:12px;height:18px;border-radius:2px;background:#f0b42a"></span></h3>
    <p class="small-bold">Potato Salad $4 | Fire Roasted Veggies $6<br>Brown Rice, Quinoa, &amp; Kale Medley $5</p>
    <div class="band"></div>
    <h3 class="heading heading--sm">KIDS MENU <span class="food-art" role="img" aria-label="Chicken drumstick illustration" style="width:18px;height:18px;background:#d98a2a"></span></h3>
    <p class="desc" style="margin:0">All served with French Fries</p>
    <div class="item"><span>Grilled Cheese<i class="veg"></i></span><span class="leader"></span><span class="price">11</span></div>
    <div class="item"><span>Cheese Quesadilla<i class="veg"></i></span><span class="leader"></span><span class="price">11</span></div>
    <div class="item"><span>Mac &amp; Cheese<i class="veg"></i></span><span class="leader"></span><span class="price">15</span></div>
    <div class="item"><span>Chicken Tenders</span><span class="leader"></span><span class="price">16</span></div>
  </div>
</section>

</body>
</html>
```